Lanternfield Disability - Social Security Disability Attorneys

Our company is expanding to attract clients nationwide for our social security disability practice. We have a logo, but I am looking for a creative and elegant letterhead that projects an image of being technologically advanced but still professional enough for the legal field. I am looking for the "wow factor" combined with this is still professional enough for a law practice.

Requesting letterhead and business card design
Updates

Had to update and change the logo. The previous logo had a typo. Please send updates with the new logo for consideration. The letterhead and business cards should be professional enough to be used for a law firm. Thanks.

Industry/Entity Type

Law Practice, Law Firm, Healthcare Industry, Government

Colors

Designer to choose colors to be used in the design.

Requirements
Nice to have
• **Please create a vertical design for the business card**

```html
<!DOCTYPE html>
<html lang="en">
<head>
<meta charset="utf-8">
<title>Lanternfield Disability Letterhead</title>
<link rel="stylesheet" href="https://fonts.googleapis.com/css2?family=Raleway:wght@400;600;800&family=Lato:wght@400&display=swap">
<style>
  :root {
    --backdrop: #6fa3a3;
    --paper: #ffffff;
    --brand-blue: #0a72ec;
    --brand-orange: #f5800f;
    --ink: #1d1d1f;
    --ink-soft: #3a3a3e;
  }
  * { margin: 0; padding: 0; box-sizing: border-box; }
  html, body { width: 1200px; height: 800px; overflow: hidden; }
  body {
    background: var(--backdrop);
    font-family: "Raleway", sans-serif;
    color: var(--ink);
  }
  .letterhead {
    position: absolute;
    left: 330px;
    top: 18px;
    width: 540px;
    height: 764px;
    background: var(--paper);
    box-shadow: 0 6px 24px rgba(0,0,0,0.18);
    overflow: hidden;
  }
  .letterhead-art { position: absolute; inset: 0; }
  .brand-name {
    position: absolute;
    right: 48px;
    top: 104px;
    display: flex;
    align-items: center;
    gap: 8px;
    font-weight: 600;
    font-size: 22px;
    letter-spacing: 0.5px;
    color: var(--brand-blue);
    text-transform: uppercase;
  }
  .brand-mark {
    width: 12px; height: 12px; border-radius: 50%;
    background: var(--brand-orange);
  }
  .recipient {
    position: absolute;
    left: 48px;
    top: 150px;
    font-style: normal;
    font-weight: 800;
    font-size: 11.5px;
    line-height: 1.35;
  }
  .reference {
    position: absolute;
    right: 48px;
    top: 214px;
    text-align: right;
    font-size: 8.5px;
    line-height: 1.6;
    color: var(--ink-soft);
  }
  .letter-body {
    position: absolute;
    left: 48px;
    top: 266px;
    width: 420px;
    font-size: 8.6px;
    line-height: 1.65;
    color: var(--ink-soft);
  }
  .letter-body p { margin-bottom: 10px; }
  .closing {
    position: absolute;
    left: 48px;
    top: 452px;
    font-size: 8.6px;
    color: var(--ink-soft);
  }
  .signature {
    width: 110px; height: 34px; margin: 8px 0 4px;
    background: linear-gradient(90deg, #eceef0, #f6f7f8);
    border-radius: 3px;
  }
  .footer-contact {
    position: absolute;
    right: 28px;
    bottom: 14px;
    display: flex;
    gap: 20px;
    font-family: "Lato", sans-serif;
    font-size: 9px;
    line-height: 1.5;
    color: #ffffff;
  }
  .footer-contact address { font-style: normal; }
</style>
</head>
<body>
  <main class="letterhead">
    <svg class="letterhead-art" viewBox="0 0 540 764" aria-hidden="true">
      <path d="M0,0 H540 V40 Q300,90 0,60 Z" fill="var(--brand-blue)"/>
      <path d="M0,72 Q300,102 540,52" fill="none" stroke="var(--brand-orange)" stroke-width="5"/>
      <path d="M0,676 Q270,636 540,666" fill="none" stroke="var(--brand-orange)" stroke-width="5"/>
      <path d="M0,690 Q270,650 540,680 V764 H0 Z" fill="var(--brand-blue)"/>
    </svg>

    <div class="brand-name"><span class="brand-mark"></span>Lanternfield Disability</div>

    <address class="recipient">
      To<br>
      Mr. Daniel Marwick<br>
      Chief Executive Officer<br>
      Greyharbor Studio<br>
      Cedar Lane<br>
      Tampa, Florida 33602
    </address>

    <div class="reference">
      Ref LD-2094 / 06<br>
      22 March, 2024
    </div>

    <section class="letter-body">
      <p>Thank you for reaching out to our office regarding your disability claim. We have reviewed the documents you provided and prepared a summary of the next steps. Our team will contact you within five business days to schedule a consultation and discuss the evidence needed for your application.</p>
      <p>Please gather your recent medical records, a list of treating physicians and any letters you have received from the agency. These materials help us build a clear and complete case on your behalf.</p>
      <p>If you have questions before our meeting, our staff is glad to help. We look forward to working with you.</p>
    </section>

    <div class="closing">
      Yours faithfully,
      <div class="signature" role="img" aria-label="Handwritten signature"></div>
      Owen Carter Hale
    </div>

    <footer class="footer-contact">
      <div>Phone: (555) 210-4480 | Fax: (555) 210-4481<br>Email: office@lanternfieldlaw.com</div>
      <address>410 Harbor View Blvd, Suite 200<br>Tampa, FL 33602<br>www.lanternfieldlaw.com</address>
    </footer>
  </main>
</body>
</html>
```